Website design for an Italian restaurant in Amsterdam

I need a design for a client of mine. It is for Teatro Lunaverde, an Italian restaurant in Amsterdam.
We are going for a clean, modern look but we also need to realise an authentic feel.
The restaurant is located in an old movie theatre, that is where the name Teatro Lunaverde comes from.
Industry/Entity Type
Italian Restaurant
Number of Pages Required
1 page
Font styles to use
Sans Serif
Colors
Designer to choose colors to be used in the design.

```html
<!DOCTYPE html>
<html lang="en">
<head>
<meta charset="utf-8">
<title>Teatro Lunaverde – Ristorante Italiano</title>
<link rel="stylesheet" href="https://fonts.googleapis.com/css2?family=Roboto:wght@300;400;500;700&family=Cormorant+Garamond:wght@400;500;600;700&family=Great+Vibes&display=swap">
<style>
:root{
  --tan:#ad9372;
  --tan-dark:#9c8262;
  --gold:#e5b323;
  --wine:#a3283e;
  --ink:#3b3b3b;
  --muted:#8a8a8a;
  --line:#d9d2c8;
  --paper:#ffffff;
  --wood:#f3f1ee;
  --panel:#e9e6e2;
}
*{box-sizing:border-box;margin:0;padding:0}
html,body{width:1200px;height:2707px;overflow:hidden;background:var(--paper)}
body{position:relative;font-family:'Roboto',sans-serif;color:var(--ink)}

/* nav */
.site-nav{position:absolute;top:0;left:0;width:1200px;height:92px;background:var(--paper);z-index:3}
.nav-link{position:absolute;top:0;height:92px;line-height:92px;font-size:11px;color:#555;letter-spacing:.3px}
.nav-link.active{background:#efefef;padding:0 20px;left:193px}
.nav-tab{position:absolute;left:460px;top:80px;width:280px;height:40px;z-index:2}
.brand{position:absolute;left:0;width:1200px;text-align:center;z-index:4}
.brand-dot{display:block;margin:0 auto;width:22px;height:22px;border-radius:50%;background:var(--wine)}
.brand-name{font-family:'Cormorant Garamond',serif;font-weight:700;font-size:23px;color:#222;letter-spacing:.5px;margin-top:8px}

/* hero */
.hero{position:absolute;top:92px;left:0;width:1200px;height:498px;
  background:radial-gradient(ellipse at 20% 10%,#d49a45 0%,transparent 40%),linear-gradient(120deg,#5a3420 0%,#3a2418 40%,#6b4a30 70%,#2f2a26 100%)}
.hero-shade{position:absolute;left:271px;top:107px;width:659px;height:391px;background:rgba(60,40,28,.45)}
.hero-rule{position:absolute;left:478px;width:244px;height:1px;background:rgba(255,255,255,.85)}
.hero-script{position:absolute;top:252px;width:1200px;text-align:center;font-family:'Great Vibes',cursive;font-size:66px;color:#fff}
.hero-title{position:absolute;top:352px;width:1200px;text-align:center;font-family:'Cormorant Garamond',serif;font-weight:400;font-size:45px;color:#fff;letter-spacing:1px}
.hero-sub{position:absolute;top:416px;width:1200px;text-align:center;font-size:14px;color:#e8e0d6;line-height:19px}

/* reserve bar */
.reserve-bar{position:absolute;top:590px;left:0;width:1200px;height:74px;background:var(--tan)}
.reserve-title{position:absolute;left:182px;top:14px;color:#fff;font-size:21px;font-weight:500;line-height:22px}
.reserve-title small{display:block;font-size:15px;font-weight:300}
.reserve-divider{position:absolute;left:298px;top:0;width:2px;height:74px;background:#fff}
.field-label{position:absolute;top:27px;color:#fff;font-size:15px}
.field{position:absolute;top:22px;height:32px;background:#bca584;color:#f3ece2;font-size:13px;line-height:32px;padding-left:20px}
.btn-gold{position:absolute;background:var(--gold);color:#fff;font-size:13px;font-weight:500;text-align:center}

/* section headings */
.section-title{position:absolute;width:1200px;text-align:center;font-family:'Cormorant Garamond',serif;font-weight:500;font-size:23px;color:#555;letter-spacing:1px}
.section-rule{position:absolute;left:540px;width:120px;height:1px;background:#c8c0b4}

/* specials grid */
.specials{position:absolute;left:202px;top:828px;width:796px;height:320px;display:grid;grid-template-columns:repeat(5,1fr);grid-template-rows:repeat(2,160px)}
.dish-photo{width:100%;height:100%}
.dish-card{background:linear-gradient(180deg,#fafafa,#eeeeee);text-align:center;padding:44px 14px 0}
.dish-card h3{font-size:13px;font-weight:400;color:#555;letter-spacing:.5px}
.dish-card p{font-size:9px;color:#999;line-height:12px;margin-top:14px}

/* sunday banner */
.sunday{position:absolute;left:200px;top:1244px;width:798px;height:204px;border:4px solid var(--tan);padding:6px}
.sunday-inner{position:relative;width:100%;height:100%;background:var(--tan);overflow:hidden}
.sunday-photo{position:absolute;right:0;top:0;width:380px;height:100%;clip-path:polygon(22% 0,100% 0,100% 100%,0 100%);background:linear-gradient(135deg,#f2efe9 0%,#c9bfae 35%,#3b3732 70%,#191919 100%)}
.sunday-lead{position:absolute;left:46px;top:42px;color:#fff;font-size:31px;font-weight:300}
.sunday-day{position:absolute;left:46px;top:77px;color:#fff;font-size:33px;font-weight:700}
.hours{position:absolute;top:122px;color:#fff;font-size:13px;line-height:16px}

/* menu */
.menu-section{position:absolute;top:1534px;left:0;width:1200px;height:623px;background:linear-gradient(90deg,#f1efec,#f7f6f4 50%,#efede9)}
.menu-photo{position:absolute;left:0;top:0;width:208px;height:430px;background:linear-gradient(160deg,#e3cf96 0%,#ebe0c2 45%,#efebe4 100%)}
.tab{position:absolute;top:1680px;font-size:13px;color:#666;height:24px;line-height:24px}
.tab.active{border:1px solid #777;border-radius:3px;padding:0 18px;left:390px}
.menu-cats{position:absolute;left:310px;top:1756px}
.menu-cat{position:absolute;left:0;font-size:14px;font-weight:500;color:#444;white-space:nowrap}
.cat-highlight{position:absolute;left:256px;top:1789px;width:246px;height:43px;background:#e4e1dc}
.menu-panel{position:absolute;left:502px;top:1742px;width:440px;height:316px;background:var(--panel)}
.menu-item{position:absolute;left:20px;width:400px}
.menu-item h4{font-size:14px;font-weight:500;color:#333}
.menu-item p{font-size:10.5px;color:#888;line-height:14px;margin-top:3px;width:300px}
.menu-item .price{position:absolute;right:20px;top:0;font-size:14px;font-weight:500;color:#333}

/* testimonials */
.avatar{position:absolute;border-radius:50%}
.avatar.main{left:300px;top:2220px;width:117px;height:117px;border:4px solid #e3d7c6;background:radial-gradient(circle at 50% 40%,#e9e3dc,#bfb4a6)}
.avatar.side{width:78px;height:78px;top:2242px;background:#ececec;opacity:.7}
.quote-title{position:absolute;left:446px;top:2238px;font-family:'Cormorant Garamond',serif;font-weight:700;font-size:16px;color:#222}
.quote-body{position:absolute;left:446px;top:2266px;width:480px;font-family:'Cormorant Garamond',serif;font-size:11.5px;line-height:16px;color:#666}
.quote-name{position:absolute;left:653px;top:2306px;font-family:'Cormorant Garamond',serif;font-weight:700;font-size:11px;color:#333}
.rating{position:absolute;left:713px;top:2306px;width:101px;height:13px;border-radius:7px;background:var(--gold)}
.pager{position:absolute;top:2380px;height:4px;width:81px;background:#d6d6d6}
.pager.active{background:var(--gold)}

/* footer */
.site-footer{position:absolute;top:2444px;left:0;width:1200px;height:263px;background:var(--tan);color:#fff}
.footer-brand{position:absolute;left:150px;width:270px;top:60px;text-align:center}
.footer-brand .brand-dot{background:#fff;width:24px;height:24px}
.footer-brand .brand-name{color:#fff;font-size:22px;margin-top:12px}
.footer-h{position:absolute;top:30px;font-size:17px;font-weight:500}
.input{position:absolute;left:480px;width:238px;background:#fff;border-radius:4px;font-size:10px;color:#aaa;padding:6px 12px}
.address{position:absolute;left:848px;top:67px;font-size:10px;line-height:18px}
.social{position:absolute;top:157px;width:16px;height:16px;border-radius:50%;background:#fff}
.footer-line{position:absolute;left:0;top:235px;width:1200px;height:1px;background:rgba(255,255,255,.6)}
.copyright{position:absolute;top:244px;width:1200px;text-align:center;font-size:9px}
</style>
</head>
<body>

<header class="site-nav">
  <span class="nav-link active">HOME</span>
  <span class="nav-link" style="left:282px">MENU</span>
  <span class="nav-link" style="left:350px">GROUP MENU</span>
  <span class="nav-link" style="left:762px">RESERVATION</span>
  <span class="nav-link" style="left:874px">CONTACT</span>
  <span class="nav-link" style="left:962px">BLOG</span>
</header>
<svg class="nav-tab" viewBox="0 0 280 40" aria-hidden="true"><path d="M0 0H280L250 40H30Z" fill="#fff"/></svg>
<div class="brand" style="top:14px">
  <span class="brand-dot"></span>
  <div class="brand-name">TEATRO LUNAVERDE</div>
</div>

<section class="hero" role="img" aria-label="Warm-lit restaurant dining room with string lights and set tables">
  <div class="hero-shade"></div>
</section>
<div class="hero-rule" style="top:236px"></div>
<div class="hero-script">Welcome to</div>
<h1 class="hero-title">TEATRO LUNAVERDE</h1>
<p class="hero-sub">The Italian restaurant located in the heart of<br>Amsterdam</p>
<div class="hero-rule" style="top:484px"></div>

<section class="reserve-bar">
  <div class="reserve-title">RESERVE<small>YOUR TABLE</small></div>
  <div class="reserve-divider"></div>
  <span class="field-label" style="left:347px">Guests</span>
  <div class="field" style="left:417px;width:161px">no. of guests
    <svg style="position:absolute;right:12px;top:9px" width="18" height="14" viewBox="0 0 18 14"><circle cx="6" cy="4" r="3" fill="#fff"/><circle cx="13" cy="4" r="2.5" fill="#fff"/><path d="M0 13c0-4 3-5 6-5s6 1 6 5z" fill="#fff"/><path d="M11 8c3 0 7 1 7 5h-5z" fill="#fff"/></svg>
  </div>
  <span class="field-label" style="left:607px">When</span>
  <div class="field" style="left:662px;width:232px">select date
    <svg style="position:absolute;right:12px;top:9px" width="14" height="14" viewBox="0 0 14 14"><rect x="1" y="2" width="12" height="11" fill="none" stroke="#fff" stroke-width="1.5"/><path d="M1 5h12M4 0v3M10 0v3" stroke="#fff" stroke-width="1.5"/></svg>
  </div>
  <div class="btn-gold" style="left:919px;top:20px;width:99px;height:34px;line-height:34px">RESERVE</div>
</section>

<h2 class="section-title" style="top:730px">MONTHLY SPECIAL</h2>
<div class="section-rule" style="top:771px"></div>

<section class="specials">
  <div class="dish-photo" role="img" aria-label="Farfalle pasta with braised beef" style="background:linear-gradient(135deg,#d9a85a,#7a4a26)"></div>
  <div class="dish-card"><h3>LOREM IPSUM</h3><p>Fresh pasta with herbs, olive oil and parmesan.</p></div>
  <div class="dish-photo" role="img" aria-label="Seafood spaghetti with prawns" style="background:linear-gradient(135deg,#c85a2e,#3a4a55)"></div>
  <div class="dish-card"><h3>LOREM IPSUM</h3><p>Fresh pasta with herbs, olive oil and parmesan.</p></div>
  <div class="dish-photo" role="img" aria-label="Spaghetti with meatballs in tomato sauce" style="background:linear-gradient(135deg,#e0b46a,#a8321f)"></div>
  <div class="dish-card"><h3>LOREM IPSUM</h3><p>Fresh pasta with herbs, olive oil and parmesan.</p></div>
  <div class="dish-photo" role="img" aria-label="Seared tuna salad with greens" style="background:linear-gradient(135deg,#b23a3a,#5d7a3a)"></div>
  <div class="dish-card"><h3>LOREM IPSUM</h3><p>Fresh pasta with herbs, olive oil and parmesan.</p></div>
  <div class="dish-photo" role="img" aria-label="Tagliatelle in tomato sauce on a white plate" style="background:linear-gradient(135deg,#f1ece4,#d4682e)"></div>
  <div class="dish-card"><h3>LOREM IPSUM</h3><p>Fresh pasta with herbs, olive oil and parmesan.</p></div>
</section>

<section class="sunday">
  <div class="sunday-inner">
    <div class="sunday-photo" role="img" aria-label="Chef plating dishes in the kitchen"></div>
    <div class="sunday-lead">NOW WE'RE OPEN ON</div>
    <div class="sunday-day">SUNDAYS</div>
    <div class="hours" style="left:46px">Tue - Sun<br>Mon</div>
    <div class="hours" style="left:155px">18:00 - 23:00<br>Closed</div>
    <div class="btn-gold" style="left:299px;top:123px;width:168px;height:33px;line-height:33px;font-size:14px;font-weight:400">RESERVE A TABLE</div>
  </div>
</section>

<section class="menu-section">
  <div class="menu-photo" role="img" aria-label="Raw pasta, tomatoes, pepper and mushrooms on a wooden table"></div>
</section>
<h2 class="section-title" style="top:1587px">MENU</h2>
<div class="section-rule" style="top:1627px"></div>
<span class="tab active">Foods</span>
<span class="tab" style="left:511px">Beverages</span>
<span class="tab" style="left:637px">Wines</span>
<span class="tab" style="left:740px">Deserts</span>
<div class="cat-highlight"></div>
<div class="menu-cats">
  <span class="menu-cat" style="top:2px">Le Insalate</span>
  <span class="menu-cat" style="top:44px">Antipasti</span>
  <span class="menu-cat" style="top:87px">Le Paste</span>
  <span class="menu-cat" style="top:130px">Il Pesce</span>
  <span class="menu-cat" style="top:174px">La Carne</span>
  <span class="menu-cat" style="top:215px">Contorni</span>
  <span class="menu-cat" style="top:258px">Dolce</span>
</div>
<div class="menu-panel">
  <div class="menu-item" style="top:14px"><h4>Pane Burro e Tapanada</h4><p>Bread, garlicbutter and olivetapenade</p><span class="price">€ 4,50</span></div>
  <div class="menu-item" style="top:66px"><h4>Carpaccio di Manzo</h4><p>Thinly sliced tenderloin with a pesto of rocketsalad and parmesan cheese</p><span class="price">€ 13,50</span></div>
  <div class="menu-item" style="top:134px"><h4>Carpaccio di Tonno</h4><p>Thinly sliced tuna with red onion, capers and rocketsalad</p><span class="price">€ 14,50</span></div>
  <div class="menu-item" style="top:185px"><h4>Vitello Tonnato</h4><p>Thinly sliced veal with Piemonte tunasauce and large capers</p><span class="price">€ 14,75</span></div>
  <div class="menu-item" style="top:236px"><h4>Antipasto Italiano</h4><p>San Daniele ham, pikante salami, Italiaanse worst, italiaanse kazen, burrata en olijven (min. 2 pers.)</p><span class="price">€ 16,00</span></div>
</div>

<section>
  <div class="avatar side" role="img" aria-label="Guest portrait" style="left:99px"></div>
  <div class="avatar main" role="img" aria-label="Portrait of the reviewing guest"></div>
  <div class="avatar side" role="img" aria-label="Guest portrait" style="left:1023px"></div>
  <h3 class="quote-title">Lorem ipsum dolor sit amet, consectetur adipiscing elit.</h3>
  <p class="quote-body">Wonderful evening in a beautiful old cinema hall. The pasta was fresh, the wine list generous and the staff warm and attentive. We will certainly come back with friends.</p>
  <span class="quote-name">- Jane Doe</span>
  <span class="rating"></span>
  <span class="pager" style="left:471px"></span>
  <span class="pager active" style="left:558px"></span>
  <span class="pager" style="left:644px"></span>
</section>

<footer class="site-footer">
  <div class="footer-brand">
    <span class="brand-dot"></span>
    <div class="brand-name">TEATRO LUNAVERDE</div>
  </div>
  <h4 class="footer-h" style="left:480px">Contact Us</h4>
  <div class="input" style="top:59px;height:24px">Your name</div>
  <div class="input" style="top:88px;height:22px">Email</div>
  <div class="input" style="top:115px;height:67px">Message</div>
  <div class="btn-gold" style="left:639px;top:191px;width:79px;height:22px;line-height:22px;font-size:10px;border-radius:3px">SEND</div>
  <h4 class="footer-h" style="left:848px">Address</h4>
  <div class="address">Teatro Lunaverde<br>Lindengracht 42<br>1015KZ Amsterdam<br>Tel nr.: (+31) 20 555 0192</div>
  <span class="social" style="left:851px"></span>
  <span class="social" style="left:884px"></span>
  <span class="social" style="left:918px"></span>
  <div class="footer-line"></div>
  <div class="copyright">Copyright teatrolunaverde.info. All Right Reserved.</div>
</footer>

</body>
</html>
```